Brivolt VoIP COMMERCIAL PHONE FLYER

We are a full service telecom VoIP company that offers local, long distance calling plans to business clients. We offer local installations, and local service we have a hands on approach and will match or beat any competitor. We work with all types of business. We are fully HIPPA complient in the medical field

Target Market(s)

SMALL TO MEDIUM BUSINESS, Medical, Real Estate, Lawyer, Accounting

Industry/Entity Type

VoIP

Font styles to use
Serif

Colors
0054AA
0677BA
7BADD7
CADEEF
E8F1F8

Requirements
Must have
• Modern/ Current picture of phone reader friendly
Nice to have
• free flow, friendly, modern
Should not have
• stuffy, corporate feel

```html
<!DOCTYPE html>
<html lang="en">
<head>
<meta charset="utf-8">
<title>Brivolt VoIP Flyer</title>
<link href="https://fonts.googleapis.com/css2?family=Alfa+Slab+One&family=Montserrat:wght@400;500;600;700;800&display=swap" rel="stylesheet">
<style>
:root{
  --blue-deep:#0054AA;
  --blue-mid:#0677BA;
  --blue-soft:#7BADD7;
  --blue-pale:#CADEEF;
  --blue-mist:#E8F1F8;
  --navy:#1b3c86;
  --band:#2a4f9c;
  --feature:#5b86cc;
  --white:#ffffff;
  --stage:#e3e7ef;
}
*{margin:0;padding:0;box-sizing:border-box}
html,body{width:1200px;height:899px;overflow:hidden}
body{background:var(--stage);font-family:"Montserrat",sans-serif;color:var(--white);position:relative}
.flyer{position:absolute;left:342px;top:86px;width:515px;height:727px;background:var(--blue-deep);overflow:hidden;box-shadow:0 10px 30px rgba(20,40,90,.25)}
.hero{position:absolute;left:0;top:0;width:515px;height:358px}
.hero-photo{position:absolute;inset:0;background:linear-gradient(100deg,#6d8fc6 0%,#5a80c0 35%,#3f67b0 70%,#4c73b8 100%)}
.hero-shade{position:absolute;inset:0;background:linear-gradient(180deg,rgba(0,60,150,.15),rgba(0,60,150,.35))}
.device-photo{position:absolute;left:262px;top:98px;width:253px;height:232px;border-radius:10px;background:linear-gradient(160deg,#2a2d33 0%,#1a1c20 60%,#3a3d44 100%)}
.device-photo .screen{position:absolute;left:12px;top:30px;width:176px;height:128px;border-radius:3px;background:linear-gradient(135deg,var(--blue-pale),var(--blue-soft))}
.logo-badge{position:absolute;left:25px;top:0;width:113px;height:102px}
.logo-badge svg{position:absolute;inset:0}
.logo-name{position:absolute;left:0;top:26px;width:113px;text-align:center;font-family:"Montserrat",sans-serif;font-weight:800;font-size:18px;color:var(--blue-mid);letter-spacing:.5px}
.call-label{position:absolute;right:14px;top:16px;font-size:10px;font-weight:700;letter-spacing:.3px}
.call-number{position:absolute;right:14px;top:30px;font-size:35px;font-weight:600;letter-spacing:.5px}
.headline{position:absolute;left:25px;top:146px;width:225px;font-family:"Alfa Slab One",serif;font-weight:400;line-height:1}
.headline .line-1{font-size:22px;display:block}
.headline .line-2{font-size:30px;display:block;margin-top:9px;color:var(--blue-mist)}
.headline .line-3{font-size:58px;display:block;margin-top:2px;color:var(--blue-mist)}
.headline .line-4{font-size:16px;display:block;margin-top:6px;margin-left:2px}
.cloud{position:absolute;left:0;top:358px;width:515px;height:104px;background:rgba(123,173,215,.85);text-align:center;padding:10px 30px 0}
.cloud h2{font-family:"Alfa Slab One",serif;font-weight:400;font-size:22px;letter-spacing:.3px}
.cloud p{font-size:9.6px;line-height:1.3;margin-top:7px}
.savings{position:absolute;left:0;top:462px;width:515px;height:130px;background:var(--band)}
.savings-copy{position:absolute;left:25px;top:20px;width:228px;font-family:"Alfa Slab One",serif;line-height:1}
.savings-copy .kicker{font-size:17px;display:block}
.savings-copy .big{font-size:32px;display:block;margin-top:8px;color:var(--blue-pale)}
.savings-copy .tail{font-size:11.5px;display:block;margin-top:8px}
.savings-divider{position:absolute;left:260px;top:16px;height:96px;border-left:2px dashed var(--white)}
.savings-figure{position:absolute;left:276px;top:8px;width:230px;text-align:center;font-size:96px;font-weight:700;line-height:1.15}
.features{position:absolute;left:0;top:592px;width:515px;height:67px;background:var(--feature);border-top:2px dashed var(--white);border-bottom:2px dashed var(--white);display:flex}
.feature{flex:1;display:flex;align-items:center;justify-content:center;gap:12px;font-weight:700;font-size:13px;line-height:1.15}
.feature + .feature{border-left:2px dashed var(--white);margin:6px 0}
.feature svg{width:34px;height:34px;flex:none}
.social{position:absolute;left:0;top:659px;width:515px;height:68px;background:var(--navy);display:flex;align-items:center;justify-content:space-around;padding:0 14px}
.social-item{display:flex;align-items:center;gap:20px;font-size:14px;font-weight:500;letter-spacing:.3px}
.social-dot{width:30px;height:30px;border-radius:50%;background:var(--blue-soft)}
</style>
</head>
<body>
<main class="flyer">
  <section class="hero">
    <div class="hero-photo" role="img" aria-label="Photo of a businesswoman talking on an office phone"></div>
    <div class="hero-shade"></div>
    <div class="device-photo" role="img" aria-label="Photo of a modern desk video phone showing a video call"><div class="screen"></div></div>
    <div class="logo-badge">
      <svg viewBox="0 0 113 102" aria-hidden="true"><polygon points="0,0 113,0 113,74 56.5,102 0,74" fill="#ffffff"/></svg>
      <div class="logo-name">BRIVOLT</div>
    </div>
    <p class="call-label">CALL TODAY FOR YOUR FREE PHONES :</p>
    <p class="call-number">123-456-7890</p>
    <h1 class="headline">
      <span class="line-1">WE OFFER FREE</span>
      <span class="line-2">TELEPHONE</span>
      <span class="line-3">LINES</span>
      <span class="line-4">FOR YOUR BUSINESS</span>
    </h1>
  </section>

  <section class="cloud">
    <h2>YOUR BUSINESS ON THE CLOUD</h2>
    <p>We are a full service telecom VoIP company that offers local, long distance calling plans to business clients. We offer local installations, and local service we have a hands on approach and will match or beat any competitor. We work with all types of business. We are fully HIPPA complient in the medical field</p>
  </section>

  <section class="savings">
    <div class="savings-copy">
      <span class="kicker">WE HELP COMPANIES</span>
      <span class="big">SAVE OVER</span>
      <span class="tail">ON THEIR MOTHLY PHONE BILLS</span>
    </div>
    <div class="savings-divider"></div>
    <div class="savings-figure">35%</div>
  </section>

  <section class="features">
    <div class="feature">
      <svg viewBox="0 0 34 34" aria-hidden="true"><circle cx="17" cy="17" r="15" fill="none" stroke="#fff" stroke-width="2"/><path d="M19 6 L10 19 H16 L14 28 L24 14 H18 Z" fill="#fff"/></svg>
      <span>Powerful<br>Features</span>
    </div>
    <div class="feature">
      <svg viewBox="0 0 34 34" aria-hidden="true"><path d="M13 30 V12 a2.5 2.5 0 0 1 5 0 V19 l7 1.5 a3 3 0 0 1 2.3 3.4 L26 30" fill="none" stroke="#fff" stroke-width="2" stroke-linejoin="round"/><path d="M9 11 a6.5 6.5 0 0 1 13 0" fill="none" stroke="#fff" stroke-width="2"/></svg>
      <span>Easy<br>To Use</span>
    </div>
    <div class="feature">
      <svg viewBox="0 0 34 34" aria-hidden="true"><path d="M6 28 L20 14" stroke="#fff" stroke-width="3" stroke-linecap="round"/><circle cx="23" cy="11" r="5" fill="none" stroke="#fff" stroke-width="2"/><path d="M8 6 L28 26" stroke="#fff" stroke-width="2" stroke-linecap="round"/></svg>
      <span>Easy<br>Set Up</span>
    </div>
  </section>

  <footer class="social">
    <div class="social-item"><span class="social-dot"></span><span>BRIVOLT</span></div>
    <div class="social-item"><span class="social-dot"></span><span>BRIVOLT</span></div>
    <div class="social-item"><span class="social-dot"></span><span>BRIVOLT</span></div>
  </footer>
</main>
</body>
</html>
```